Tallowmere Contracting Business Cards

Front of card:

Full Logo
Name
Address
Office Phone
Cell Phone
Email
Website

Back:
Logo Mark in background
List and markets and services performed

```html
<!DOCTYPE html>
<html lang="en">
<head>
<meta charset="utf-8">
<title>Tallowmere Contracting Business Cards</title>
<link href="https://fonts.googleapis.com/css2?family=Montserrat:wght@400;500;700&display=swap" rel="stylesheet">
<style>
  :root {
    --brand-red: #d6262a;
    --brand-grey: #7a7a7a;
    --ink: #1c1c1c;
    --paper: #ffffff;
    --backdrop: #3a3735;
  }
  * { box-sizing: border-box; margin: 0; padding: 0; }
  html, body { width: 1200px; height: 900px; overflow: hidden; }
  body {
    background: var(--backdrop);
    font-family: 'Montserrat', sans-serif;
    display: flex;
    flex-direction: column;
    align-items: center;
    justify-content: center;
    gap: 40px;
  }
  .card {
    position: relative;
    width: 665px;
    height: 380px;
    overflow: hidden;
    box-shadow: 0 10px 30px rgba(0,0,0,0.45);
  }

  /* Back side */
  .card-back { background: var(--brand-red); color: var(--paper); }
  .card-back .wordmark {
    position: absolute;
    left: 0; right: 0; top: 120px;
    display: flex; align-items: center; justify-content: center; gap: 20px;
  }
  .mark-circle {
    width: 92px; height: 92px; border-radius: 50%;
    border: 8px solid currentColor;
    flex: none;
  }
  .wordmark-text {
    font-weight: 700;
    text-transform: uppercase;
    line-height: 1.05;
    letter-spacing: 2px;
  }
  .card-back .wordmark-text { font-size: 34px; }
  .wordmark-text .llc { display: block; font-size: 0.5em; text-align: right; letter-spacing: 4px; }
  .tagline {
    position: absolute; left: 0; right: 0; bottom: 60px;
    text-align: center; font-size: 15px; font-weight: 400; letter-spacing: 0.3px;
  }

  /* Front side */
  .card-front { background: var(--paper); }
  .wave { position: absolute; inset: 0; }
  .card-front .wordmark {
    position: absolute; left: 50px; top: 88px; width: 220px;
    display: flex; flex-direction: column; align-items: center; gap: 14px;
    color: var(--brand-red);
  }
  .card-front .mark-circle { width: 86px; height: 86px; border-width: 7px; }
  .card-front .wordmark-text { font-size: 22px; text-align: center; letter-spacing: 1px; }
  .divider {
    position: absolute; left: 300px; top: 60px;
    width: 2px; height: 160px; background: var(--brand-red);
  }
  .contact { position: absolute; left: 322px; top: 52px; color: var(--ink); }
  .person-name { font-size: 19px; font-weight: 700; text-transform: uppercase; letter-spacing: 0.5px; }
  .person-name .first { color: var(--brand-red); }
  .person-name .last { color: var(--brand-grey); }
  .person-role { font-size: 13px; margin: 2px 0 10px; }
  .contact-list { list-style: none; font-size: 12.5px; font-weight: 500; }
  .contact-list li { display: flex; align-items: center; gap: 9px; height: 22px; }
  .contact-list svg { width: 13px; height: 13px; fill: var(--brand-red); flex: none; }
</style>
</head>
<body>

<section class="card card-back">
  <div class="wordmark">
    <span class="mark-circle"></span>
    <div class="wordmark-text">Tallowmere<br>Contracting<span class="llc">LLC</span></div>
  </div>
  <p class="tagline">List and markets and services performed</p>
</section>

<section class="card card-front">
  <svg class="wave" viewBox="0 0 665 380" preserveAspectRatio="none" aria-hidden="true">
    <path d="M0,352 C200,346 320,312 412,232 C500,156 585,132 665,126 L665,380 L0,380 Z" fill="var(--brand-grey)"/>
    <path d="M0,346 C200,340 318,306 408,226 C496,150 580,126 665,120 L665,128 C585,134 504,158 418,236 C326,318 206,352 0,358 Z" fill="var(--paper)"/>
    <path d="M0,364 C210,358 340,326 430,248 C516,174 592,150 665,146 L665,380 L0,380 Z" fill="var(--brand-red)"/>
  </svg>

  <div class="wordmark">
    <span class="mark-circle"></span>
    <div class="wordmark-text">Tallowmere<br>Contracting<span class="llc">LLC</span></div>
  </div>

  <div class="divider"></div>

  <div class="contact">
    <p class="person-name"><span class="first">Marcus</span> <span class="last">Hale</span></p>
    <p class="person-role">Co-Founder</p>
    <ul class="contact-list">
      <li><svg viewBox="0 0 16 16"><path d="M3 1h3l1 4-2 1c1 2 3 4 5 5l1-2 4 1v3c0 1-1 2-2 2C7 15 1 9 1 3c0-1 1-2 2-2z"/></svg>555-201-3347</li>
      <li><svg viewBox="0 0 16 16"><path d="M4 0h8c1 0 1.5.5 1.5 1.5v13c0 1-.5 1.5-1.5 1.5H4c-1 0-1.5-.5-1.5-1.5v-13C2.5.5 3 0 4 0zm0 2v10h8V2zm4 11a1 1 0 100 2 1 1 0 000-2z"/></svg>555-418-7702</li>
      <li><svg viewBox="0 0 16 16"><path d="M0 3h16v1L8 9 0 4zm0 3l8 5 8-5v7H0z"/></svg>info@tallowmerecontractingllc.com</li>
      <li><svg viewBox="0 0 16 16"><path d="M8 0a8 8 0 100 16A8 8 0 008 0zm0 2c1 1.5 1.6 3.3 1.7 5H6.3C6.4 5.3 7 3.5 8 2zM2.1 9h2.2c.1 1.7.6 3.3 1.3 4.6A6 6 0 012.1 9zm0-2a6 6 0 013.5-4.6C4.9 3.7 4.4 5.3 4.3 7zm4.2 2h3.4c-.1 1.7-.7 3.5-1.7 5-1-1.5-1.6-3.3-1.7-5zm4.1 4.6c.7-1.3 1.2-2.9 1.3-4.6h2.2a6 6 0 01-3.5 4.6zM11.7 7c-.1-1.7-.6-3.3-1.3-4.6A6 6 0 0113.9 7z"/></svg>www.tallowmerecontractingllc.com</li>
      <li><svg viewBox="0 0 16 16"><path d="M8 0a5.5 5.5 0 015.5 5.5C13.5 10 8 16 8 16S2.5 10 2.5 5.5A5.5 5.5 0 018 0zm0 3a2.5 2.5 0 100 5 2.5 2.5 0 000-5z"/></svg>42-10 Cedar Row 8, Fairbrook</li>
    </ul>
  </div>
</section>

</body>
</html>
```